Year 12 Chemistry Workbook illustrations and diagrams

We are producing a Chemistry Workbook for senior high-school students in South Australia and require a designer to create illustrations including detailed diagrams and graphs for our upcoming publication.

The attached files are illustrations that we'd like to have recreated, with your own personal style incorporated.

We will require you to do the following:
- Create vector artwork
- Supply AI files
- Use the font helvetica neue 45 light, or its italic variation
- Use full colour wherever possible
- Please use 100% black, not RGB black/eye-dropped black

Target Market(s)

Senior high school students

Industry/Entity Type

School

Font styles to use
Sans Serif

Colors

Designer to choose colors to be used in the design.

Requirements
Must have
• - Create vector artwork
• - Supply AI files
• - Use the font helvetica neue 45 light, or its italic variation
• - Use full colour wherever possible
• - Please use 100% black, not RGB black/eye-dropped black
Should not have
• Please do not use RGB black/eye-dropped black

```html
<!DOCTYPE html>
<html lang="en">
<head>
<meta charset="utf-8">
<title>Biofuel Production Diagrams</title>
<link rel="stylesheet" href="https://fonts.googleapis.com/css2?family=Inter:wght@300;400&display=swap">
<style>
  :root {
    --ink: #000000;
    --paper: #ffffff;
    --orange: #F8AE3A;
    --purple-1: #A87CC0;
    --purple-2: #C6A8D6;
    --purple-3: #E4D3EB;
    --blue-1: #1565E8;
    --blue-2: #6FA6F5;
    --blue-3: #CFE2FB;
    --ester-blue: #1414E0;
    --magenta: #E6307A;
    --tan: #C79E6B;
    --tan-light: #EEE0CB;
  }
  html, body { margin: 0; padding: 0; overflow: hidden; background: var(--paper); }
  .canvas { width: 1200px; height: 1200px; }
  .canvas svg { display: block; width: 1200px; height: 1200px; }
  text { font-family: "Inter", "Helvetica Neue", Arial, sans-serif; font-weight: 300; fill: var(--ink); }
  .label { font-size: 17px; }
  .small { font-size: 13px; }
  .box-label { font-size: 19px; }
  .line { stroke: var(--ink); stroke-width: 3; fill: none; }
  .thin { stroke: var(--ink); stroke-width: 1.5; fill: none; }
  .stage { stroke: var(--ink); stroke-width: 3; }
  .step { fill: var(--tan); stroke: var(--ink); stroke-width: 2; }
  .step-light { fill: var(--tan-light); stroke: var(--ink); stroke-width: 2; }
  .ester-box { fill: none; stroke: var(--ester-blue); stroke-width: 3; }
  .glycerol-box { fill: none; stroke: var(--magenta); stroke-width: 3; }
  .ester-path { stroke: var(--ester-blue); stroke-width: 2; stroke-dasharray: 7 6; fill: none; }
  .glycerol-path { stroke: var(--magenta); stroke-width: 2; stroke-dasharray: 7 6; fill: none; }
</style>
</head>
<body>
<div class="canvas">
<svg viewBox="0 0 1500 1500" xmlns="http://www.w3.org/2000/svg">
  <defs>
    <marker id="head" viewBox="0 0 10 10" refX="8" refY="5" markerWidth="5" markerHeight="5" orient="auto-start-reverse">
      <path d="M0 0 L10 5 L0 10 z" fill="#000"/>
    </marker>
    <marker id="head-thin" viewBox="0 0 10 10" refX="9" refY="5" markerWidth="8" markerHeight="8" orient="auto">
      <path d="M0 1 L10 5 L0 9" fill="none" stroke="#000" stroke-width="1.5"/>
    </marker>
    <marker id="head-blue" viewBox="0 0 10 10" refX="8" refY="5" markerWidth="6" markerHeight="6" orient="auto">
      <path d="M0 0 L10 5 L0 10 z" fill="#1414E0"/>
    </marker>
    <marker id="head-pink" viewBox="0 0 10 10" refX="8" refY="5" markerWidth="6" markerHeight="6" orient="auto">
      <path d="M0 0 L10 5 L0 10 z" fill="#E6307A"/>
    </marker>
    <linearGradient id="apparatus-fill" x1="0" y1="0" x2="0" y2="1">
      <stop offset="0" stop-color="#BFE3F5"/>
      <stop offset="0.5" stop-color="#2BA6E0"/>
      <stop offset="1" stop-color="#D1B93A"/>
    </linearGradient>
  </defs>

  <!-- Heating apparatus -->
  <g class="apparatus">
    <rect x="245" y="40" width="225" height="475" rx="16" fill="url(#apparatus-fill)" role="img" aria-label="Illustration of a beaker of water with a thermometer, on a stand heated by a spirit burner with fuel"/>
    <text class="label" x="90" y="80">Thermometer</text>
    <line class="thin" x1="237" y1="80" x2="310" y2="90"/>
    <text class="label" x="146" y="203">Beaker</text>
    <line class="thin" x1="232" y1="198" x2="303" y2="206"/>
    <text class="label" x="156" y="283">Water</text>
    <line class="thin" x1="232" y1="274" x2="328" y2="274"/>
    <text class="label" x="108" y="449">Spirit Burner</text>
    <line class="thin" x1="230" y1="445" x2="290" y2="460"/>
    <text class="label" x="178" y="490">Fuel</text>
    <line class="thin" x1="232" y1="484" x2="300" y2="484"/>
  </g>

  <!-- Biodiesel process flow -->
  <g class="biodiesel-flow">
    <text class="label" x="693" y="172" text-anchor="middle">Oil</text>
    <line class="line" x1="648" y1="182" x2="746" y2="182" marker-end="url(#head)"/>
    <text class="label" x="693" y="245" text-anchor="middle">Alcohol +</text>
    <line class="line" x1="650" y1="260" x2="748" y2="260" marker-end="url(#head)"/>
    <text class="label" x="685" y="284" text-anchor="middle">Catalyst</text>
    <text class="label" x="692" y="309" text-anchor="middle">(e.g. Methoxide)</text>

    <rect class="stage" x="764" y="118" width="102" height="220" fill="var(--orange)"/>
    <text class="label" transform="translate(809 228) rotate(90)" text-anchor="middle">Transesterification</text>
    <line class="line" x1="871" y1="182" x2="913" y2="182" marker-end="url(#head)"/>

    <rect class="stage" x="920" y="118" width="94" height="154" fill="var(--orange)"/>
    <text class="label" transform="translate(985 193) rotate(90)" text-anchor="middle">Mixed</text>
    <text class="label" transform="translate(964 193) rotate(90)" text-anchor="middle">Methyl</text>
    <text class="label" transform="translate(943 193) rotate(90)" text-anchor="middle">Esters</text>
    <line class="line" x1="1019" y1="182" x2="1059" y2="182" marker-end="url(#head)"/>

    <rect class="stage" x="1066" y="118" width="54" height="130" fill="var(--purple-1)"/>
    <text class="label" transform="translate(1087 183) rotate(90)" text-anchor="middle">Separator</text>
    <line class="line" x1="1093" y1="112" x2="1093" y2="74" marker-end="url(#head)"/>
    <text class="label" x="1093" y="62" text-anchor="middle">Alcohol</text>
    <line class="line" x1="1125" y1="182" x2="1166" y2="182" marker-end="url(#head)"/>

    <rect class="stage" x="1173" y="118" width="54" height="130" fill="var(--purple-2)"/>
    <text class="label" transform="translate(1205 183) rotate(90)" text-anchor="middle">Extraction</text>
    <text class="label" transform="translate(1184 183) rotate(90)" text-anchor="middle">Using Water</text>
    <line class="line" x1="1200" y1="72" x2="1200" y2="110" marker-end="url(#head)"/>
    <text class="label" x="1198" y="62" text-anchor="middle">Water</text>
    <path class="line" d="M1200 256 V276 H1258" marker-end="url(#head)"/>
    <text class="label" x="1268" y="283">Wash Water</text>
    <line class="line" x1="1232" y1="182" x2="1273" y2="182" marker-end="url(#head)"/>

    <rect class="stage" x="1280" y="118" width="54" height="130" fill="var(--purple-3)"/>
    <text class="label" transform="translate(1301 183) rotate(90)" text-anchor="middle">Separator</text>
    <line class="line" x1="1307" y1="112" x2="1307" y2="74" marker-end="url(#head)"/>
    <text class="label" x="1307" y="63" text-anchor="middle">Water</text>
    <line class="line" x1="1385" y1="155" x2="1342" y2="155" marker-end="url(#head)"/>
    <text class="label" x="1421" y="150" text-anchor="middle">Heat &amp;</text>
    <text class="label" x="1421" y="171" text-anchor="middle">Vacuum</text>
    <line class="line" x1="1340" y1="214" x2="1383" y2="214" marker-end="url(#head)"/>
    <text class="label" x="1395" y="220">Biodiesel</text>

    <path class="line" d="M966 280 V398 H1008" marker-end="url(#head)"/>
    <text class="label" x="922" y="336" text-anchor="middle">Crude</text>
    <text class="label" x="924" y="357" text-anchor="middle">Glycerol</text>

    <rect class="stage" x="1014" y="360" width="54" height="130" fill="var(--blue-1)"/>
    <text class="label" transform="translate(1035 425) rotate(90)" text-anchor="middle">Separator</text>
    <line class="line" x1="1041" y1="352" x2="1041" y2="310" marker-end="url(#head)"/>
    <text class="label" x="1041" y="300" text-anchor="middle">Alcohol</text>
    <line class="line" x1="960" y1="447" x2="1008" y2="447" marker-end="url(#head)"/>
    <text class="label" x="921" y="444" text-anchor="middle">Heat &amp;</text>
    <text class="label" x="921" y="466" text-anchor="middle">Vacuum</text>
    <line class="line" x1="1073" y1="447" x2="1113" y2="447" marker-end="url(#head)"/>

    <rect class="stage" x="1119" y="360" width="54" height="130" fill="var(--blue-2)"/>
    <text class="label" transform="translate(1140 425) rotate(90)" text-anchor="middle">Water Wash</text>
    <line class="line" x1="1146" y1="310" x2="1146" y2="350" marker-end="url(#head)"/>
    <text class="label" x="1146" y="301" text-anchor="middle">Water</text>
    <line class="line" x1="1178" y1="447" x2="1219" y2="447" marker-end="url(#head)"/>

    <rect class="stage" x="1225" y="360" width="54" height="130" fill="var(--blue-3)"/>
    <text class="label" transform="translate(1246 425) rotate(90)" text-anchor="middle">Neutralizer</text>
    <path class="line" d="M1298 330 H1254 V350" marker-end="url(#head)"/>
    <text class="label" x="1348" y="330" text-anchor="middle">Neutralized</text>
    <text class="label" x="1348" y="352" text-anchor="middle">Glycerol</text>
    <line class="line" x1="1284" y1="447" x2="1324" y2="447" marker-end="url(#head)"/>
    <text class="label" x="1332" y="453">Acid</text>
  </g>

  <!-- Transesterification equation -->
  <g class="equation">
    <rect class="glycerol-box" x="545" y="566" width="75" height="346"/>
    <text class="label" x="585" y="616" text-anchor="middle">CH<tspan font-size="12" dy="4">2</tspan></text>
    <text class="label" x="583" y="745" text-anchor="middle">CH</text>
    <text class="label" x="585" y="868" text-anchor="middle">CH<tspan font-size="12" dy="4">2</tspan></text>
    <line class="thin" x1="583" y1="626" x2="583" y2="725"/>
    <line class="thin" x1="583" y1="752" x2="583" y2="848"/>
    <line class="thin" x1="620" y1="612" x2="634" y2="612"/>
    <line class="thin" x1="620" y1="739" x2="634" y2="739"/>
    <line class="thin" x1="620" y1="866" x2="634" y2="866"/>

    <rect class="ester-box" x="634" y="566" width="130" height="96"/>
    <text class="label" x="692" y="592" text-anchor="middle">O</text>
    <text class="label" x="692" y="615" text-anchor="middle">||</text>
    <text class="label" x="652" y="640">O – C – R<tspan font-size="11" dy="4">1</tspan></text>

    <rect class="ester-box" x="634" y="691" width="130" height="96"/>
    <text class="label" x="692" y="717" text-anchor="middle">O</text>
    <text class="label" x="692" y="740" text-anchor="middle">||</text>
    <text class="label" x="651" y="765">O – C – R<tspan font-size="11" dy="4">2</tspan></text>

    <rect class="ester-box" x="634" y="816" width="130" height="96"/>
    <text class="label" x="692" y="842" text-anchor="middle">O</text>
    <text class="label" x="692" y="865" text-anchor="middle">||</text>
    <text class="label" x="652" y="890">O – C – R<tspan font-size="11" dy="4">3</tspan></text>

    <path class="ester-path" d="M772 615 C840 560 940 570 1014 600" marker-end="url(#head-blue)"/>
    <path class="ester-path" d="M772 738 C840 690 940 695 1014 722" marker-end="url(#head-blue)"/>
    <path class="ester-path" d="M774 866 C840 820 940 825 1016 853" marker-end="url(#head-blue)"/>

    <text class="label" x="770" y="755">+ &#160; 3CH<tspan font-size="11" dy="4">3</tspan><tspan dy="-4">OH</tspan></text>
    <line class="line" x1="910" y1="753" x2="1013" y2="753" marker-end="url(#head)"/>
    <text class="label" x="963" y="775" text-anchor="middle">NaOh</text>
    <text class="label" x="963" y="797" text-anchor="middle">Catalyst</text>

    <rect class="ester-box" x="1023" y="560" width="194" height="352" rx="30"/>
    <text class="label" x="1146" y="592" text-anchor="middle">O</text>
    <text class="label" x="1146" y="614" text-anchor="middle">||</text>
    <text class="label" x="1037" y="638">CH<tspan font-size="11" dy="4">3</tspan><tspan dy="-4"> – &#160;O &#160;– C – R</tspan><tspan font-size="11" dy="4">1</tspan></text>
    <text class="label" x="1146" y="706" text-anchor="middle">O</text>
    <text class="label" x="1146" y="728" text-anchor="middle">||</text>
    <text class="label" x="1037" y="751">CH<tspan font-size="11" dy="4">3</tspan><tspan dy="-4"> – &#160;O &#160;– C – R</tspan><tspan font-size="11" dy="4">2</tspan></text>
    <text class="label" x="1146" y="838" text-anchor="middle">O</text>
    <text class="label" x="1146" y="860" text-anchor="middle">||</text>
    <text class="label" x="1037" y="883">CH<tspan font-size="11" dy="4">3</tspan><tspan dy="-4"> – &#160;O &#160;– C – R</tspan><tspan font-size="11" dy="4">3</tspan></text>

    <text class="label" x="1235" y="751" text-anchor="middle">+</text>

    <rect class="glycerol-box" x="1252" y="566" width="144" height="346"/>
    <text class="label" x="1281" y="616">CH<tspan font-size="12" dy="4">2</tspan><tspan dy="-4"> &#160;– OH</tspan></text>
    <text class="label" x="1283" y="745">CH &#160; – OH</text>
    <text class="label" x="1281" y="866">CH<tspan font-size="12" dy="4">2</tspan><tspan dy="-4"> &#160;– OH</tspan></text>
    <line class="thin" x1="1296" y1="626" x2="1296" y2="725"/>
    <line class="thin" x1="1296" y1="752" x2="1296" y2="846"/>

    <path class="glycerol-path" d="M558 918 V975 H1276 V920" marker-end="url(#head-pink)"/>
    <text class="small" x="582" y="960">Triglyceride</text>
    <text class="label" x="860" y="960" text-anchor="middle">Methanol</text>
    <text class="label" x="1127" y="963" text-anchor="middle">Mixture of Fatty Esters</text>
    <text class="label" x="1336" y="963" text-anchor="middle">Glycerin</text>
  </g>

  <!-- Ethanol from sugarcane -->
  <g class="sugarcane-flow">
    <polygon points="302,1018 258,1018 258,1038 252,1038 268,1052 284,1038 278,1038 278,1030 302,1030" fill="var(--ink)"/>
    <text class="small" x="307" y="1028" font-size="15">Sugarcane</text>
    <rect class="step" x="226" y="1057" width="100" height="39"/>
    <text class="box-label" x="276" y="1083" text-anchor="middle">Milling</text>
    <line class="thin" x1="330" y1="1076" x2="347" y2="1076" marker-end="url(#head-thin)"/>
    <rect class="step" x="351" y="1057" width="169" height="39"/>
    <text class="box-label" x="436" y="1083" text-anchor="middle">Pretreatment</text>
    <line class="thin" x1="524" y1="1076" x2="542" y2="1076" marker-end="url(#head-thin)"/>
    <rect class="step" x="546" y="1057" width="126" height="39"/>
    <text class="box-label" x="609" y="1083" text-anchor="middle">Filtration</text>
    <line class="thin" x1="676" y1="1076" x2="694" y2="1076" marker-end="url(#head-thin)"/>
    <rect class="step" x="698" y="1057" width="180" height="39"/>
    <text class="box-label" x="788" y="1083" text-anchor="middle">Fermentation</text>
    <line class="thin" x1="882" y1="1076" x2="900" y2="1076" marker-end="url(#head-thin)"/>
    <rect class="step" x="904" y="1057" width="152" height="39"/>
    <text class="box-label" x="980" y="1083" text-anchor="middle">Distillation</text>
    <line class="thin" x1="1062" y1="1076" x2="1164" y2="1076" marker-end="url(#head-thin)"/>
    <text class="small" x="1110" y="1071" text-anchor="middle" font-size="15">Dehydration</text>
    <text class="box-label" x="1175" y="1083">Ethanol</text>

    <line class="thin" x1="272" y1="1098" x2="272" y2="1128" marker-end="url(#head-thin)"/>
    <text class="small" x="285" y="1119" font-size="15">Bagasse</text>
    <text class="small" x="272" y="1150" text-anchor="middle" font-size="15">Boiler</text>
    <line class="thin" x1="604" y1="1098" x2="604" y2="1128" marker-end="url(#head-thin)"/>
    <text class="small" x="601" y="1150" text-anchor="middle" font-size="15">Cake</text>
    <line class="thin" x1="782" y1="1128" x2="782" y2="1098" marker-end="url(#head-thin)"/>
    <text class="small" x="783" y="1150" text-anchor="middle" font-size="15">Yeast</text>
  </g>

  <!-- Ethanol from dry ground corn -->
  <g class="corn-flow">
    <polygon points="297,1198 253,1198 253,1218 247,1218 263,1232 279,1218 273,1218 273,1210 297,1210" fill="var(--ink)"/>
    <text class="small" x="305" y="1208" font-size="15">Dry Ground</text>
    <text class="small" x="328" y="1227" font-size="15">Corn</text>
    <rect class="step-light" x="221" y="1237" width="102" height="39"/>
    <text class="box-label" x="272" y="1263" text-anchor="middle">Milling</text>
    <line class="thin" x1="327" y1="1256" x2="345" y2="1256" marker-end="url(#head-thin)"/>
    <rect class="step-light" x="349" y="1237" width="170" height="39"/>
    <text class="box-label" x="434" y="1263" text-anchor="middle">Liquefaction</text>
    <line class="thin" x1="523" y1="1256" x2="541" y2="1256" marker-end="url(#head-thin)"/>
    <rect class="step-light" x="545" y="1237" width="326" height="39"/>
    <text class="box-label" x="708" y="1263" text-anchor="middle">Hydrolysis &amp; Fermentation</text>
    <line class="thin" x1="875" y1="1256" x2="895" y2="1256" marker-end="url(#head-thin)"/>
    <rect class="step-light" x="899" y="1237" width="169" height="39"/>
    <text class="box-label" x="984" y="1263" text-anchor="middle">Distillation</text>
    <line class="thin" x1="1075" y1="1256" x2="1175" y2="1256" marker-end="url(#head-thin)"/>
    <text class="small" x="1121" y="1250" text-anchor="middle" font-size="15">Dehydration</text>
    <text class="box-label" x="1183" y="1263">Ethanol</text>

    <line class="thin" x1="434" y1="1306" x2="434" y2="1278" marker-end="url(#head-thin)"/>
    <text class="small" x="434" y="1325" text-anchor="middle" font-size="15">Enzyme</text>
    <line class="thin" x1="628" y1="1306" x2="628" y2="1278" marker-end="url(#head-thin)"/>
    <text class="small" x="628" y="1325" text-anchor="middle" font-size="15">Enzyme</text>
    <line class="thin" x1="769" y1="1306" x2="769" y2="1278" marker-end="url(#head-thin)"/>
    <text class="small" x="769" y="1325" text-anchor="middle" font-size="15">Yeast</text>
    <line class="thin" x1="984" y1="1278" x2="984" y2="1306" marker-end="url(#head-thin)"/>
    <text class="small" x="984" y="1332" text-anchor="middle" font-size="15">Solids</text>
    <line class="thin" x1="984" y1="1343" x2="984" y2="1373" marker-end="url(#head-thin)"/>
    <text class="small" x="1005" y="1364" font-size="15">Drying</text>
    <text class="small" x="984" y="1397" text-anchor="middle" font-size="15">Distillers Dry Grains</text>
  </g>
</svg>
</div>
</body>
</html>
```